Lorne Hollow Farm Postcard Design

I am looking for a new postcard design to mail out this season. We are a Farm business that does wholesale and retail and bulk seasoned firewood sales. we sell firewood from anything from bagged wood to tractor trailer loads of wood. We sell firewood in bulk bags. Pick up or delivery available there is no order to big or too small. I need my business name and phone number on the cards Lorne Hollow Farm 848-316-0572 (call or text) I would like it to say we are the best priced guaranteed. I want something that is simple and straight forward but also really catches the eye when they see these in the mail box. I attached my logo and feel free to use photos of split firewood if you would like. id like my email on the card Lornehollowfarm90@mailvista.net.

Target Market(s)

Firewood purchasers

Industry/Entity Type

agriculture

Requirements
Must have
• email phone number logo

```html
<!DOCTYPE html>
<html lang="en">
<head>
<meta charset="utf-8">
<title>Lorne Hollow Farm Postcard</title>
<link href="https://fonts.googleapis.com/css2?family=Anton&family=Archivo+Black&family=Poppins:wght@400;500;600;700;800&display=swap" rel="stylesheet">
<style>
:root{
  --stage:#b9b9b9;
  --dark:#1d1d1d;
  --orange:#ef4e12;
  --amber:#f7a81b;
  --yellow:#fdc10e;
  --red:#e8341c;
  --ink:#1f1f1f;
  --white:#ffffff;
  --rule:#bdbdbd;
  --stamp:#e4e4e4;
}
*{margin:0;padding:0;box-sizing:border-box}
html,body{width:900px;height:1200px;overflow:hidden;background:var(--stage)}
body{position:relative;font-family:'Poppins',sans-serif;color:var(--ink)}
.card{position:absolute;left:58px;width:784px;height:523px;background:var(--white);overflow:hidden;box-shadow:0 4px 14px rgba(0,0,0,.25)}
.card--front{top:56px}
.card--back{top:620px}
.card-art{position:absolute;inset:0}
.abs{position:absolute}

/* front */
.brand-name{left:41px;top:40px;width:128px;font-weight:800;font-size:19px;line-height:22px;color:var(--amber);text-align:center}
.badge-text{left:194px;width:149px;text-align:center;color:var(--white);font-weight:600}
.badge-top{top:30px;font-size:14px;line-height:18px}
.badge-free{top:44px;font-family:'Archivo Black',sans-serif;font-size:44px;line-height:46px;color:var(--ink)}
.badge-bottom{top:85px;font-size:14px;line-height:18px}
.headline-1{left:41px;top:158px;font-family:'Archivo Black',sans-serif;font-size:22.5px;color:var(--white);letter-spacing:.3px}
.headline-2{left:41px;top:182px;font-family:'Archivo Black',sans-serif;font-size:34px;color:var(--white)}
.headline-3{left:41px;top:216px;font-family:'Anton',sans-serif;font-size:54px;line-height:66px;letter-spacing:-.5px;background:linear-gradient(180deg,var(--yellow) 10%,var(--orange) 60%,var(--red));-webkit-background-clip:text;background-clip:text;color:transparent}
.feature{top:321px;font-size:14px;line-height:17px;font-weight:500;color:var(--white)}
.feature--one{left:56px;width:150px}
.feature--two{left:230px;width:168px}
.feature-dot{position:absolute;left:-15px;top:4px;width:9px;height:9px;border-radius:50%;background:#8c2a08;border:2px solid #c0410f}
.call-label{left:41px;top:431px;font-size:23px;font-weight:400;line-height:28px}
.call-label b,.back-call b{color:var(--orange);font-weight:700}
.call-number{left:41px;top:456px;font-size:25px;font-weight:600;letter-spacing:.5px}
.mail-line{display:flex;align-items:center;gap:9px;font-weight:500;white-space:nowrap}
.front-mail{left:245px;top:446px;font-size:20px}
.mail-icon{width:18px;height:13px;flex:none}
.follow{left:666px;top:440px;font-size:15px;font-weight:500;text-align:center;width:82px;white-space:nowrap}
.follow-mark{display:block;width:14px;height:14px;background:var(--orange);margin:6px auto 0;border-radius:2px}

/* back */
.services-title{left:49px;top:33px;font-weight:700;font-size:16.5px;color:var(--amber);letter-spacing:.2px}
.service-list{left:49px;top:64px;width:330px;display:grid;grid-template-columns:172px 158px;row-gap:8.5px;list-style:none}
.service-list li{display:flex;align-items:center;gap:8px;font-weight:600;font-size:13.3px;color:var(--white);height:22px;white-space:nowrap}
.service-icon{width:22px;height:22px;border-radius:50%;background:var(--red);flex:none;display:flex;align-items:center;justify-content:center}
.service-icon i{width:9px;height:9px;border:1.5px solid var(--white);border-radius:2px}
.promise{left:49px;top:202px;color:var(--white);font-size:15.5px;line-height:20px}
.promise b{font-weight:700}
.guaranteed{left:162px;top:200px;font-family:'Anton',sans-serif;font-size:41px;line-height:48px;color:var(--yellow)}
.back-call{left:38px;top:412px;font-size:24px;font-weight:400;white-space:nowrap}
.back-call span{font-weight:600;letter-spacing:.5px}
.back-mail{left:38px;top:444px;font-size:21px}
.back-mail .mail-icon{width:19px;height:14px}
.mini-brand{left:468px;top:32px;width:79px;height:68px;background:#111;display:flex;align-items:center;justify-content:center;text-align:center;font-weight:800;font-size:11px;line-height:13px;color:var(--amber);padding:4px}
.stamp-box{left:686px;top:37px;width:64px;height:57px;background:var(--stamp)}
.address-rule{left:463px;width:285px;height:1px;background:var(--rule)}
</style>
</head>
<body>

<section class="card card--front">
  <svg class="card-art" width="784" height="523" viewBox="0 0 784 523">
    <defs>
      <linearGradient id="ringGrad" x1="0" y1="0" x2="0" y2="1">
        <stop offset="0" stop-color="#fdc10e"/>
        <stop offset=".6" stop-color="#f7811b"/>
        <stop offset="1" stop-color="#ef4e12"/>
      </linearGradient>
      <linearGradient id="woodsGrad" x1="0" y1="0" x2="0" y2="1">
        <stop offset="0" stop-color="#d9d9d6"/>
        <stop offset=".45" stop-color="#8c8478"/>
        <stop offset="1" stop-color="#9a9690"/>
      </linearGradient>
      <linearGradient id="truckGrad" x1="0" y1="0" x2="1" y2="1">
        <stop offset="0" stop-color="#8a1a22"/>
        <stop offset=".6" stop-color="#5a1218"/>
        <stop offset="1" stop-color="#2a2a2e"/>
      </linearGradient>
      <linearGradient id="shieldGrad" x1="0" y1="0" x2="0" y2="1">
        <stop offset="0" stop-color="#e4b47c"/>
        <stop offset="1" stop-color="#c88e55"/>
      </linearGradient>
    </defs>
    <rect x="0" y="0" width="784" height="298" fill="#1d1d1d"/>
    <rect x="0" y="305" width="784" height="117" fill="#ef4e12"/>
    <circle cx="680" cy="94" r="284" fill="url(#ringGrad)"/>
    <circle cx="680" cy="94" r="272" fill="#ffffff"/>
    <circle cx="680" cy="94" r="264" fill="url(#woodsGrad)" role="img" aria-label="Photo of a tree service yard with bare trees, logs and equipment"/>
    <rect x="404" y="256" width="380" height="182" rx="14" fill="url(#truckGrad)" role="img" aria-label="Photo of a red semi truck cab"/>
    <path d="M194 0 V122 L268.5 142 L343 122 V0 Z" fill="url(#shieldGrad)"/>
    <path d="M202 0 V116 L268.5 134 L335 116 V0" fill="none" stroke="#8a5d31" stroke-width="1.5" opacity=".6"/>
    <line x1="242" y1="107" x2="295" y2="107" stroke="#ffffff" stroke-width="1.5"/>
  </svg>

  <div class="abs brand-name">Lorne Hollow Farm</div>

  <div class="abs badge-text badge-top">FULLY INSURED</div>
  <div class="abs badge-text badge-free">FREE</div>
  <div class="abs badge-text badge-bottom">ESTIMATES</div>

  <h1>
    <span class="abs headline-1">WHOLESALE AND RETAIL</span>
    <span class="abs headline-2">BULK SEASONED</span>
    <span class="abs headline-3">FIREWOOD SALES</span>
  </h1>

  <p class="abs feature feature--one"><span class="feature-dot"></span>We sell firewood from anything from bagged wood to tractor trailer loads of wood.</p>
  <p class="abs feature feature--two"><span class="feature-dot"></span>We sell firewood in bulk bags. Pick up or delivery available there is no order to big or too small.</p>

  <div class="abs call-label"><b>CALL</b> OR <b>TEXT</b></div>
  <div class="abs call-number">848-316-0572</div>

  <div class="abs mail-line front-mail">
    <svg class="mail-icon" viewBox="0 0 18 13"><rect width="18" height="13" fill="#ef4e12"/><path d="M0 0 L9 7 L18 0 M0 13 L7 6 M18 13 L11 6" stroke="#ffffff" stroke-width="1.4" fill="none"/></svg>
    <span>Lornehollowfarm90@mailvista.net</span>
  </div>

  <div class="abs follow">follow us<span class="follow-mark"></span></div>
</section>

<section class="card card--back">
  <svg class="card-art" width="784" height="523" viewBox="0 0 784 523">
    <defs>
      <linearGradient id="backRing" x1="0" y1="0" x2="0" y2="1">
        <stop offset="0" stop-color="#fdc10e"/>
        <stop offset=".6" stop-color="#f7811b"/>
        <stop offset="1" stop-color="#ef4e12"/>
      </linearGradient>
      <linearGradient id="logsGrad" x1="0" y1="0" x2="0" y2="1">
        <stop offset="0" stop-color="#c9c9c4"/><stop offset="1" stop-color="#5a4a38"/>
      </linearGradient>
      <linearGradient id="splitterGrad" x1="0" y1="0" x2="1" y2="1">
        <stop offset="0" stop-color="#1f5a34"/><stop offset="1" stop-color="#c98a1e"/>
      </linearGradient>
      <linearGradient id="crewGrad" x1="0" y1="0" x2="0" y2="1">
        <stop offset="0" stop-color="#8a6a4a"/><stop offset="1" stop-color="#6b5a45"/>
      </linearGradient>
    </defs>
    <circle cx="157" cy="118" r="285" fill="#111111"/>
    <circle cx="157" cy="118" r="283" fill="url(#backRing)"/>
    <circle cx="157" cy="118" r="258" fill="#ffffff"/>
    <circle cx="157" cy="118" r="248" fill="#1d1d1d"/>
    <circle cx="100" cy="330" r="69" fill="url(#logsGrad)" stroke="#f7a81b" stroke-width="7" role="img" aria-label="Photo of cut logs on a trailer"/>
    <circle cx="220" cy="331" r="60" fill="url(#splitterGrad)" stroke="#f7a81b" stroke-width="7" role="img" aria-label="Photo of a firewood processing machine"/>
    <circle cx="333" cy="330" r="54" fill="url(#crewGrad)" stroke="#f7a81b" stroke-width="7" role="img" aria-label="Photo of a worker carrying a log"/>
  </svg>

  <h2 class="abs services-title">SERVICES WE PROVIDE</h2>
  <ul class="abs service-list">
    <li><span class="service-icon"><i></i></span>Tree removal</li>
    <li><span class="service-icon"><i></i></span>Mulch</li>
    <li><span class="service-icon"><i></i></span>Tree trimming</li>
    <li><span class="service-icon"><i></i></span>Spring clean ups</li>
    <li><span class="service-icon"><i></i></span>Stump grinding</li>
    <li><span class="service-icon"><i></i></span>Gravel</li>
    <li><span class="service-icon"><i></i></span>Stone</li>
    <li><span class="service-icon"><i></i></span>Landscaping</li>
  </ul>

  <p class="abs promise">WE ARE THE<br><b>BEST PRICED</b></p>
  <div class="abs guaranteed">GUARANTEED</div>

  <div class="abs back-call"><b>CALL</b> OR <b>TEXT:</b> <span>848-316-0572</span></div>
  <div class="abs mail-line back-mail">
    <svg class="mail-icon" viewBox="0 0 18 13"><rect width="18" height="13" fill="#ef4e12"/><path d="M0 0 L9 7 L18 0 M0 13 L7 6 M18 13 L11 6" stroke="#ffffff" stroke-width="1.4" fill="none"/></svg>
    <span>Lornehollowfarm90@mailvista.net</span>
  </div>

  <div class="abs mini-brand">Lorne Hollow Farm</div>
  <div class="abs stamp-box"></div>
  <div class="abs address-rule" style="top:218px"></div>
  <div class="abs address-rule" style="top:266px"></div>
  <div class="abs address-rule" style="top:313px"></div>
  <div class="abs address-rule" style="top:360px"></div>
</section>

</body>
</html>
```